Infographic Design for Aluminium Can Recycling

We require a neat design that can be integrated into print advertising for a 'cash for cans' recycling promotion and also scaled back for Facebook promotion. The promotion is aimed at kids/families. Needs to be fresh and colourful - but also appealing to children. The flyer is to be designed at A5 size and also at FB post sizing. You can just submit the one design in A5 to win, with the knowledge that you will need to redesign slightly later to suit FB post size.

The design needs to contain as much of the following as possible.

- The best thing is - Aluminium is 100% recyclable FOREVER
- If you recycled just one can everyday for a week, you'd save enough energy to watch TV straight for 21 hours - thats an entire season of XXX
- 105,784 cans are recycled every minute
- it takes the same amount of energy to make 1 new can as it does to recycle 20
- a recycled can is back on the shelf in 60 days
-2/3 of the aluminium ever produced is still in use today

Please keep colours muted - not bright
Please do not present anything like the 'Tidy Loop' lie attached. This is far too busy.
I have attached the original flyer for information only (see below for what to and what NOT to include)
I've attached some cute graphics I think kids and adults will find appealing. Design something similar. The prize to be won is an electric scooter - perhaps they could be riding this.

They are giving away an electric Scooter (not Bike)

Please use Pellbrook Alloy Traders and LOGO

Please provide address and details of event as per flyer

Please leave out the following text:
HEY KIDS
WIN THIS BIKE
FIND US ON FB
LUCKY DOOR PRIZE + SAUSAGE SIZZLE
WE PAY CASH FOR CANS
Collect as many aluminium cans as you can and bring them to our can day and get paid for cash
Do not include the can man graphic

Please have information:
Event location
Win an Electric Scooter
Turn in your CANS for CASH

Great - can't wait to see what you creative geniuses come back with!!
Updates

None of these designs matched the brief. Im actually not sure what to do now?

Target Market(s)

Males 35+

Industry/Entity Type

Advertising

Font styles to use
Sans Serif

Colors
5c5c5c
0555a3
3276b5
b1b1b1
faa54b
fbf289
33a6d7
f04a50

Requirements
Must have
• Please read brief
Nice to have
• Please see brief
Should not have
• Please see brief

```html
<!DOCTYPE html>
<html lang="en">
<head>
<meta charset="utf-8">
<title>Turn in your Cans for Cash – Pellbrook Alloy Traders</title>
<link rel="stylesheet" href="https://fonts.googleapis.com/css2?family=Roboto:wght@400;500;700;900&family=Ubuntu:wght@500;700&display=swap">
<style>
  :root {
    --page-bg: #ece6df;
    --flyer-bg: #dce6bb;
    --ink: #1d5a78;
    --banner: #0f5170;
    --deep-green: #1e6b2c;
    --grass: #3e8e3a;
    --arrow: #a8cb8c;
    --orange: #e8893c;
    --orange-dark: #d96d20;
    --donut-light: #eec082;
    --can-blue: #3496c9;
    --calendar-red: #a63a32;
    --sky-top: #e4f2f3;
    --sky-bottom: #b9dce2;
    --bin-green: #5aa43c;
    --logo-blue: #2b5aa5;
  }
  * { box-sizing: border-box; margin: 0; padding: 0; }
  html, body { width: 1200px; height: 1000px; overflow: hidden; }
  body {
    position: relative;
    background: var(--page-bg);
    font-family: "Roboto", Arial, sans-serif;
    color: var(--ink);
  }
  .flyer {
    position: absolute; left: 262px; top: 28px;
    width: 676px; height: 945px;
    background: var(--flyer-bg);
    box-shadow: 0 2px 10px rgba(0,0,0,.12);
  }
  .shapes { position: absolute; left: 0; top: 0; width: 1200px; height: 1000px; }
  .abs { position: absolute; }

  .headline-top {
    left: 262px; width: 676px; top: 72px; text-align: center;
    font-family: "Ubuntu", sans-serif; font-weight: 700; font-size: 38px;
    color: var(--ink); letter-spacing: .5px;
  }
  .headline-main {
    left: 430px; width: 340px; top: 126px; text-align: center;
    font-family: "Ubuntu", sans-serif; font-weight: 500; font-size: 46px;
    color: #fff; line-height: 56px;
  }

  .scene {
    left: 262px; top: 198px; width: 676px; height: 196px;
    background: linear-gradient(180deg, var(--sky-top), var(--sky-bottom));
  }
  .prize-lead {
    left: 600px; width: 240px; top: 224px; text-align: center;
    font-family: "Ubuntu", sans-serif; font-weight: 700; font-size: 38px;
    color: var(--orange);
  }
  .prize-name {
    left: 540px; width: 335px; top: 272px; text-align: center;
    font-family: "Ubuntu", sans-serif; font-weight: 500; font-size: 43px;
    color: #fff; line-height: 58px;
  }

  .fact { font-size: 16px; line-height: 21px; color: var(--ink); }
  .fact b { font-weight: 700; }
  .best-lead { left: 423px; top: 446px; font-size: 22px; line-height: 25px; }
  .best-figure {
    left: 598px; top: 433px; font-weight: 900; font-size: 70px;
    line-height: 70px; color: var(--deep-green); letter-spacing: -3px;
  }
  .best-note { left: 610px; top: 503px; font-size: 14px; }
  .best-note b { color: var(--deep-green); }
  .donut-label {
    left: 330px; width: 74px; top: 545px; text-align: center;
    font-weight: 700; font-size: 29px; color: var(--orange-dark);
  }
  .fact-still { left: 432px; top: 550px; }
  .fact-energy { left: 560px; width: 280px; top: 602px; text-align: right; }
  .can-word {
    left: 845px; width: 40px; top: 620px; text-align: center;
    font-weight: 500; font-size: 15px; color: #fff;
  }
  .fact-shelf-a { left: 302px; top: 705px; }
  .calendar-num {
    left: 572px; width: 68px; top: 690px; text-align: center;
    font-weight: 900; font-size: 36px; color: var(--calendar-red);
  }
  .fact-shelf-b { left: 645px; top: 705px; }
  .counter { left: 668px; top: 746px; display: flex; gap: 4px; }
  .counter span {
    width: 32px; height: 56px; border-radius: 4px;
    font-weight: 700; font-size: 34px; line-height: 58px;
    color: #fff; text-align: center;
    border-top: 5px solid rgba(0,0,0,.18);
  }
  .fact-minute { left: 668px; top: 807px; }
  .bin {
    left: 452px; top: 812px; width: 112px; height: 130px;
    background: linear-gradient(180deg, #6cb348, var(--bin-green));
    clip-path: polygon(0 12%, 100% 12%, 90% 100%, 10% 100%);
  }
  .fact-week { left: 565px; top: 876px; font-size: 15px; line-height: 21px; }

  .brand { left: 288px; top: 860px; width: 140px; display: flex; align-items: center; gap: 8px; }
  .brand-dot { width: 24px; height: 24px; border-radius: 50%; background: var(--logo-blue); flex: none; }
  .brand-name {
    font-weight: 700; font-size: 14px; line-height: 16px;
    color: var(--logo-blue); text-transform: uppercase;
  }
</style>
</head>
<body>
  <div class="flyer"></div>

  <div class="abs scene" role="img" aria-label="Illustration of a child riding an electric scooter with a plug cord, clouds and trees on a pale blue sky"></div>

  <svg class="shapes" viewBox="0 0 1200 1000" aria-hidden="true">
    <defs>
      <marker id="arrow-head" viewBox="0 0 10 10" refX="5" refY="5" markerWidth="3" markerHeight="3" orient="auto">
        <path d="M0 0 L10 5 L0 10z" fill="#fff"/>
      </marker>
    </defs>
    <g>
      <rect x="287" y="124" width="28" height="54" rx="5" fill="#55a383"/>
      <rect x="323" y="124" width="28" height="54" rx="5" fill="#3ba6cf"/>
      <rect x="359" y="124" width="28" height="54" rx="5" fill="#d9681f"/>
    </g>
    <polygon points="425,125 780,125 796,155 780,185 425,185 409,155" fill="none" stroke="var(--banner)" stroke-width="4"/>
    <polygon points="432,130 773,130 787,155 773,180 432,180 418,155" fill="var(--banner)"/>
    <g fill="#f0a23c" stroke="#d9802a" stroke-width="3">
      <circle cx="826" cy="151" r="18"/><circle cx="862" cy="151" r="18"/><circle cx="898" cy="151" r="18"/>
    </g>
    <g fill="#fff" font-family="Roboto, sans-serif" font-weight="700" font-size="18" text-anchor="middle">
      <text x="826" y="158">$</text><text x="862" y="158">$</text><text x="898" y="158">$</text>
    </g>

    <polygon points="488,288 545,288 545,350 488,350 510,319" fill="var(--orange-dark)"/>
    <polygon points="870,288 928,288 906,319 928,350 870,350" fill="var(--orange-dark)"/>
    <rect x="540" y="270" width="335" height="62" fill="var(--orange)"/>
    <rect x="262" y="393" width="676" height="13" fill="var(--grass)"/>

    <g fill="var(--arrow)">
      <rect x="262" y="459" width="120" height="12"/><polygon points="380,450 400,465 380,480"/>
      <rect x="832" y="560" width="106" height="12"/><polygon points="834,551 814,566 834,581"/>
      <rect x="262" y="629" width="384" height="12"/><polygon points="644,620 664,635 644,650"/>
      <rect x="710" y="709" width="228" height="12"/><polygon points="712,700 692,715 712,730"/>
      <rect x="262" y="764" width="384" height="12"/><polygon points="644,755 664,770 644,785"/>
      <rect x="760" y="849" width="178" height="12"/><polygon points="762,840 742,855 762,870"/>
    </g>

    <!-- 100% badge -->
    <line x1="760" y1="476" x2="780" y2="476" stroke="#fff" stroke-width="3"/>
    <circle cx="838" cy="476" r="62" fill="var(--deep-green)"/>
    <circle cx="838" cy="476" r="46" fill="none" stroke="#fff" stroke-width="4" stroke-dasharray="240 49"/>
    <polygon points="812,436 826,432 818,444" fill="#fff"/>
    <g stroke="#fff" stroke-width="6" fill="none" stroke-linecap="round" marker-end="url(#arrow-head)">
      <path d="M843 457 L856 480"/>
      <path d="M854 496 L828 496"/>
      <path d="M817 485 L830 462"/>
    </g>

    <circle cx="367" cy="560" r="46" fill="none" stroke="var(--donut-light)" stroke-width="22"/>
    <circle cx="367" cy="560" r="46" fill="none" stroke="var(--orange-dark)" stroke-width="22"
            stroke-dasharray="192.7 289" transform="rotate(-90 367 560) scale(1 -1) translate(0 -1120)" transform-origin="0 0"/>

    <rect x="845" y="592" width="40" height="76" rx="5" fill="var(--can-blue)"/>
    <rect x="848" y="592" width="34" height="6" rx="2" fill="#2a7fab"/>
    <path d="M880 588 l2 6 l6 2 l-6 2 l-2 6 l-2 -6 l-6 -2 l6 -2z" fill="#fff"/>

    <rect x="572" y="668" width="68" height="70" rx="8" fill="#fff"/>
    <path d="M572 676 a8 8 0 0 1 8 -8 h52 a8 8 0 0 1 8 8 v12 h-68z" fill="var(--calendar-red)"/>
    <rect x="587" y="660" width="5" height="16" rx="2" fill="#9aa0a6"/>
    <rect x="620" y="660" width="5" height="16" rx="2" fill="#9aa0a6"/>

    <path d="M578 818 C640 812 700 822 740 846" fill="none" stroke="var(--grass)" stroke-width="2" stroke-dasharray="6 5"/>
  </svg>

  <div class="abs headline-top">TURN IN YOUR</div>
  <div class="abs headline-main">CANS for CASH</div>

  <div class="abs prize-lead">Win an</div>
  <div class="abs prize-name">Electric Scooter</div>

  <div class="abs fact best-lead">The Best thing is<br>Aluminium is</div>
  <div class="abs best-figure">100%</div>
  <div class="abs fact best-note">recyclable <b>FOREVER</b></div>

  <div class="abs donut-label">2/3</div>
  <div class="abs fact fact-still">of the aluminium ever produced is still in use today</div>

  <div class="abs fact fact-energy">It takes the same amount<br>of energy to make <b>1 new</b><br>as it does to <b>recycle 20</b></div>
  <div class="abs can-word">CAN</div>

  <div class="abs fact fact-shelf-a">A recycled can is back on the shelf in</div>
  <div class="abs calendar-num">60</div>
  <div class="abs fact fact-shelf-b"><b>days</b></div>

  <div class="abs counter" aria-label="105784">
    <span style="background:#a3b32e">1</span>
    <span style="background:#3ba0c9">0</span>
    <span style="background:#a794bd">5</span>
    <span style="background:#c17f7c">7</span>
    <span style="background:#e0732a">8</span>
    <span style="background:#5aa583">4</span>
  </div>
  <div class="abs fact fact-minute">cans are recycled <b>every minute</b></div>

  <div class="abs bin" role="img" aria-label="Illustration of a green recycling bin with cans inside"></div>
  <div class="abs fact fact-week">If you recycled just <b>one can everyday for a week</b>,<br>you'd save enough energy to watch TV straight for<br>21 hours - thats an entire season of XXX</div>

  <div class="abs brand">
    <span class="brand-dot"></span>
    <span class="brand-name">Pellbrook Alloy Traders</span>
  </div>
</body>
</html>
```